Margarita Company needs Table Tent Design

Ever at a restaurant and see a mouth-watering table side advertisement for a refreshing beverage? We make Margarita Mix. We need to design a Table Tent for display on the tables in Mexican restaurants to encourage restaurant patrons to order more Copper Lantern Margaritas. Design is 2 sided - each side is 4.5" (wide) x 6" (tall).

Target Market(s)

Restaurant Patrons that are visiting a restaurant, generally Mexican restaurants.

Industry/Entity Type

Mexican Restaurant

Font styles to use
Serif

Requirements
Must have
• Mouth-watering design.
Nice to have
• Marketing copy that sells more drinks.
Should not have
• Inappropriate language or images that you wouldn't share with a parent. Also, our main goal is to help the restaurants sell more drinks so we do not usually feature our company logo but we like to add our company web address in a subtle manner.

```html
<!DOCTYPE html>
<html lang="en">
<head>
<meta charset="utf-8">
<title>Margarita Mix Table Tent</title>
<link href="https://fonts.googleapis.com/css2?family=Delius&family=Arimo:wght@400&display=swap" rel="stylesheet">
<style>
  :root{
    --bg:#ececea;
    --green-deep:#1d5a2c;
    --green-mid:#2f7a35;
    --gold:#d9a912;
    --yellow:#f1d23a;
    --pale:#eef0c8;
    --red:#c8361c;
    --orange:#e8731d;
    --white:#ffffff;
    --ink:#245a22;
  }
  *{margin:0;padding:0;box-sizing:border-box}
  html,body{width:1200px;height:1200px;overflow:hidden;background:var(--bg)}
  .canvas{position:relative;width:1200px;height:1200px}
  .panel{position:absolute;top:360px;width:360px;height:480px;overflow:hidden;box-shadow:0 6px 18px rgba(0,0,0,.18)}
  .panel--back{left:30px}
  .panel--front{left:420px}
  .panel--alt{left:810px}
  .panel svg.shapes{position:absolute;inset:0;width:100%;height:100%}
  .photo{position:absolute;left:0;top:0;width:100%}
  .title{position:absolute;font-family:"Delius",serif;color:var(--ink);white-space:nowrap}
  .url{position:absolute;font-family:"Arimo",sans-serif;color:var(--white);font-size:15px;letter-spacing:.3px}

  /* back side */
  .panel--back{background:linear-gradient(160deg,#d8321b 0%,#f08a2a 30%,#f6cf7a 55%,#f3c230 80%,#e9a81a 100%)}
  .panel--back .photo{height:100%;background:radial-gradient(circle at 45% 25%,rgba(255,244,200,.9),rgba(255,220,150,.3) 45%,transparent 70%)}
  .copy-frame{position:absolute;left:22px;top:24px;width:300px;height:386px;border:1px solid rgba(255,255,255,.8);border-radius:6px;background:rgba(255,250,225,.55)}
  .panel--back .title{left:0;right:0;top:26px;text-align:center;font-size:26px}
  .copy{position:absolute;left:34px;top:72px;width:280px;font-family:"Arimo",sans-serif;font-size:9.4px;line-height:1.38;color:var(--ink)}
  .copy p{margin-bottom:10px}
  .panel--back .url{left:12px;bottom:14px}

  /* front side */
  .panel--front{background:linear-gradient(180deg,#f4f2c4 0%,#e8ecb8 60%,#dfe6a8 100%)}
  .panel--front .photo{height:262px;background:radial-gradient(circle at 60% 40%,#fbfbf2 0%,#e7edc8 28%,#7aa83a 60%,#3f6e22 100%)}
  .panel--front .title{left:46px;top:378px;font-size:48px}
  .panel--front .url{left:12px;bottom:16px}

  /* alternate side */
  .panel--alt{background:linear-gradient(180deg,#f2f0cf 0%,#e9ecc4 100%)}
  .panel--alt .photo{height:262px;background:radial-gradient(circle at 65% 55%,#f6b03a 0%,#e98a24 35%,#b6b04a 70%,#5d8a2c 100%)}
  .panel--alt .title{left:28px;top:340px;font-size:40px}
  .panel--alt .url{right:12px;bottom:20px;font-style:italic}
</style>
</head>
<body>
<main class="canvas">

  <section class="panel panel--back">
    <div class="photo" role="img" aria-label="Soft background photo of a citrus margarita with red and orange fruit"></div>
    <svg class="shapes" viewBox="0 0 360 480" aria-hidden="true">
      <path d="M0,418 C90,395 200,405 360,385 L360,480 L0,480 Z" fill="var(--red)"/>
      <path d="M0,400 C100,385 220,395 360,372 L360,386 C220,408 100,398 0,414 Z" fill="var(--yellow)" opacity=".8"/>
    </svg>
    <div class="copy-frame"></div>
    <h2 class="title">Margarita Mix</h2>
    <div class="copy">
      <p>Cool off with a frosty margarita made the easy way. Our mix blends real lime juice with a touch of sweetness for a bright, smooth taste in every single glass you pour.</p>
      <p>Ask your server for a classic lime, strawberry or mango margarita. Served frozen or on the rocks with a salted rim and a fresh wedge of citrus.</p>
      <p>Sharing a table tonight? Order a pitcher for the group and toast to good food, good friends and good times. Every pitcher pours six generous glasses of pure sunshine.</p>
      <p>Pairs perfectly with tacos, enchiladas and fresh guacamole. Make it a large for just a little more and enjoy the taste of summer all year long.</p>
    </div>
    <span class="url">www.copperlanternmix.com</span>
  </section>

  <section class="panel panel--front">
    <div class="photo" role="img" aria-label="Photo of a frozen margarita with a salted rim and a lime slice, limes around it"></div>
    <svg class="shapes" viewBox="0 0 360 480" aria-hidden="true">
      <path d="M0,262 C90,250 200,235 360,248 L360,330 C240,318 130,338 0,340 Z" fill="var(--gold)"/>
      <path d="M0,300 C110,280 230,255 360,262 L360,285 C230,280 110,305 0,322 Z" fill="var(--green-deep)"/>
      <path d="M60,348 C160,330 260,318 360,318 L360,330 C260,330 160,340 60,348 Z" fill="var(--white)" opacity=".85"/>
      <path d="M0,278 C120,262 240,258 360,252" stroke="var(--yellow)" stroke-width="3" fill="none"/>
      <path d="M0,448 C110,420 230,430 360,440 L360,480 L0,480 Z" fill="var(--green-deep)"/>
    </svg>
    <h1 class="title">Margarita Mix</h1>
    <span class="url">www.copperlanternmix.com</span>
  </section>

  <section class="panel panel--alt">
    <div class="photo" role="img" aria-label="Photo of two orange margaritas with salted rims and citrus skewers"></div>
    <svg class="shapes" viewBox="0 0 360 480" aria-hidden="true">
      <path d="M0,258 C80,248 180,290 360,262 L360,295 C200,318 90,282 0,300 Z" fill="var(--green-deep)"/>
      <path d="M0,300 C90,284 200,318 360,296 L360,304 C200,326 90,292 0,308 Z" fill="var(--white)" opacity=".9"/>
      <path d="M0,468 C120,445 240,440 360,448 L360,480 L0,480 Z" fill="var(--green-deep)"/>
      <path d="M0,440 C140,418 250,425 360,432 L360,480 L0,480 Z" fill="var(--green-deep)" opacity="0"/>
    </svg>
    <h2 class="title">Margarita Mix</h2>
    <span class="url">www.copperlanternmix.com</span>
  </section>

</main>
</body>
</html>
```